logo for security & safety training, education consultants
Marlow Advisory Nest Pte Ltd
Professional
LIM BOON KEAT ROBERT
DIRECTOR
47 JALAN TEMBUSIRA SINGAPORE 528806
robert@marlownest-example.com
www.marlownest-example.com
Perhaps some iso logo and same award logo in dummies

```html
<!DOCTYPE html>
<html lang="en">
<head>
<meta charset="utf-8">
<title>Marlow Advisory Nest – Business Card</title>
<link rel="stylesheet" href="https://fonts.googleapis.com/css2?family=Montserrat:wght@500;700;900&display=swap">
<style>
  :root {
    --bg: #9a9a9a;
    --card: #ffffff;
    --ink: #151515;
    --brand-blue: #2a1fe0;
    --band-black: #111111;
    --on-dark: #ffffff;
  }
  * { margin: 0; padding: 0; box-sizing: border-box; }
  html, body {
    width: 1200px; height: 842px; overflow: hidden;
    background: var(--bg);
    font-family: "Montserrat", Arial, sans-serif;
  }
  .stage {
    width: 1200px; height: 842px;
    display: flex; align-items: center; justify-content: center; gap: 50px;
  }
  .card {
    position: relative;
    width: 540px; height: 310px;
    background: var(--card);
    box-shadow: 0 6px 18px rgba(0,0,0,.25);
    overflow: hidden;
  }
  .wordmark {
    display: flex; align-items: center; gap: 10px;
    color: var(--ink); font-weight: 900; letter-spacing: 1px;
  }
  .wordmark .dot { border-radius: 50%; background: var(--brand-blue); }
  .card--front { display: flex; align-items: center; justify-content: center; }
  .card--front .wordmark { font-size: 54px; }
  .card--front .dot { width: 40px; height: 40px; }
  .card--back .wordmark {
    position: absolute; left: 210px; top: 48px; font-size: 32px;
  }
  .card--back .dot { width: 24px; height: 24px; }
  .name-band {
    position: absolute; left: 0; top: 145px; width: 265px; height: 42px;
    background: var(--band-black); color: var(--on-dark);
    padding: 7px 14px 0 18px;
  }
  .name-band .name { font-size: 9.5px; font-weight: 700; letter-spacing: .3px; white-space: nowrap; }
  .name-band .role { font-size: 8px; font-weight: 500; margin-top: 4px; letter-spacing: 1px; }
  .address-block {
    position: absolute; left: 0; top: 187px; width: 265px; height: 98px;
    background: var(--brand-blue); color: var(--on-dark);
    padding: 22px 18px; font-size: 11px; font-weight: 500; line-height: 1.5;
    font-style: normal;
  }
  .contact-block {
    position: absolute; left: 272px; top: 145px; width: 268px; height: 140px;
    background: var(--brand-blue); color: var(--on-dark);
    padding: 18px 18px; list-style: none;
  }
  .contact-block li {
    display: flex; align-items: center; gap: 8px;
    font-size: 10.5px; font-weight: 500; height: 20px; white-space: nowrap;
  }
  .contact-block .icon {
    width: 13px; height: 13px; flex: none;
    background: var(--on-dark); border-radius: 50%;
    display: flex; align-items: center; justify-content: center;
  }
  .contact-block svg { width: 9px; height: 9px; }
</style>
</head>
<body>
<main class="stage">
  <section class="card card--front" aria-label="Card front">
    <div class="wordmark"><span class="dot"></span>MARLOW</div>
  </section>

  <section class="card card--back" aria-label="Card back">
    <div class="wordmark"><span class="dot"></span>MARLOW</div>

    <div class="name-band">
      <p class="name">LIM BOON KEAT ROBERT</p>
      <p class="role">DIRECTOR</p>
    </div>

    <address class="address-block">
      47 JALAN TEMBUSIRA<br>SINGAPORE 528806
    </address>

    <ul class="contact-block">
      <li><span class="icon"><svg viewBox="0 0 10 10"><path d="M2 1l2 2-1 1.2a5 5 0 0 0 2.8 2.8L7 6l2 2-1.2 1.2C4.5 9 1 5.5.8 2.2z" fill="#2a1fe0"/></svg></span>+65 61234570</li>
      <li><span class="icon"><svg viewBox="0 0 10 10"><rect x="3" y="1" width="4" height="8" rx="1" fill="#2a1fe0"/></svg></span>+65 90001234</li>
      <li><span class="icon"><svg viewBox="0 0 10 10"><rect x="1.5" y="3" width="7" height="5" fill="#2a1fe0"/><rect x="3" y="1" width="4" height="2" fill="#2a1fe0"/></svg></span>+65 6100 4486</li>
      <li><span class="icon"><svg viewBox="0 0 10 10"><rect x="1" y="2.5" width="8" height="5" fill="#2a1fe0"/><path d="M1 2.5l4 3 4-3" stroke="#fff" stroke-width=".8" fill="none"/></svg></span>robert@marlownest-example.com</li>
      <li><span class="icon"><svg viewBox="0 0 10 10"><circle cx="5" cy="5" r="3.8" fill="none" stroke="#2a1fe0" stroke-width="1"/><path d="M1.2 5h7.6M5 1.2v7.6" stroke="#2a1fe0" stroke-width=".8"/></svg></span>www.marlownest-example.com</li>
    </ul>
  </section>
</main>
</body>
</html>
```